Business Card Design Project - 2 sided

We need a business card design for a card having one business on each side (ie. two businesses on one card). Would like a design that incorporates logo, tagline and normal fields (name, position, address, phone).

Would also like an allowance for small font text along the bottom (text to be determined, but less than 50 characters).

NB. Attached logo for Verbal Bridgeworks has two variations - either can be used.

www.verbalbridgeworks.com / www.kelpora.com

```html
<!DOCTYPE html>
<html lang="en">
<head>
<meta charset="utf-8">
<title>Verbal Bridgeworks / Kelpora – Business Card</title>
<link rel="stylesheet" href="https://fonts.googleapis.com/css2?family=Open+Sans:wght@400;600;700&display=swap">
<style>
  :root{
    --navy:#27265f;
    --blue-light:#5aaed6;
    --blue-deep:#1678b0;
    --green:#8cc63f;
    --ink:#333333;
    --rule:#9a9a9a;
    --backdrop:#ece9e4;
    --card:#ffffff;
  }
  *{box-sizing:border-box;margin:0;padding:0}
  html,body{width:1200px;height:402px;overflow:hidden}
  body{background:var(--backdrop);font-family:"Open Sans",Arial,sans-serif;color:var(--ink);position:relative}

  .card{position:absolute;top:56px;width:510px;height:290px;border-radius:26px;background:var(--card);overflow:hidden;box-shadow:0 3px 10px rgba(0,0,0,.25)}
  .card--bridgeworks{left:63px}
  .card--kelpora{left:627px}
  .card__band{position:absolute;inset:0;width:510px;height:290px}

  .card__holder{position:absolute;top:22px;right:22px;color:#fff;font-size:16px;font-weight:700}
  .card__holder span{font-weight:400;font-size:13px}

  .brand{position:absolute;display:flex;align-items:center;gap:8px}
  .brand__name{font-weight:600;line-height:1}
  .brand__tagline{position:absolute;font-size:10.5px;font-weight:600;line-height:1}

  .card--bridgeworks .brand{left:36px;top:130px}
  .card--bridgeworks .brand__name{font-size:27px;color:var(--navy);letter-spacing:.5px}
  .card--bridgeworks .brand__tagline{left:36px;top:160px;color:#222}

  .card--kelpora .brand{left:44px;top:100px}
  .card--kelpora .brand__mark{width:40px;height:40px;border-radius:50%;background:var(--green)}
  .card--kelpora .brand__name{font-size:40px;color:var(--blue-deep)}
  .card--kelpora .brand__tagline{left:108px;top:148px;font-size:12px;letter-spacing:.6px;color:#333;font-weight:400}

  .contact{position:absolute;left:34px;top:188px;font-size:13px;line-height:17.5px}
  .contact li{list-style:none;display:flex;align-items:center;gap:6px}
  .contact svg{width:10px;height:10px;fill:var(--green);flex:none}

  .address,.extra{position:absolute;top:240px;font-size:12.5px;line-height:17.5px;padding-left:8px;border-left:1px solid var(--rule)}
  .address{left:187px}
  .extra{left:332px;font-size:11.5px;letter-spacing:.2px}
</style>
</head>
<body>

<section class="card card--bridgeworks">
  <svg class="card__band" viewBox="0 0 510 290" aria-hidden="true">
    <path d="M0 0H510V140C420 92 270 40 0 34Z" fill="var(--navy)"/>
    <path d="M0 40C120 26 250 32 390 70C250 40 120 38 0 54Z" fill="var(--green)"/>
  </svg>
  <p class="card__holder">Your Name <span>/ Title</span></p>
  <div class="brand"><span class="brand__name">Verbal Bridgeworks</span></div>
  <p class="brand__tagline">Website Translation and Localisation Specialist...</p>
  <ul class="contact">
    <li><svg viewBox="0 0 10 10"><path d="M2 0l2 2-1 1.5c.6 1.3 1.6 2.3 2.9 2.9L7 5l2 2-1.4 1.8C4 8.6 1.3 6 1 2.3Z"/></svg>123-456-7890</li>
    <li><svg viewBox="0 0 10 10"><rect x="2.5" y="0" width="5" height="10" rx="1"/></svg>123-456-7890</li>
    <li><svg viewBox="0 0 10 10"><path d="M0 4h10v2H7V5H3v1H0Z"/><rect x="2" y="6" width="6" height="4" rx="1"/></svg>123-456-7890</li>
    <li><svg viewBox="0 0 10 10"><path d="M0 2h10v6H0Z"/></svg>name@website.com</li>
    <li><svg viewBox="0 0 10 10"><circle cx="5" cy="5" r="5"/></svg>www.website.com</li>
  </ul>
  <p class="address">Complex name, Street<br>City, State, zip code</p>
  <p class="extra">xxxxxxxxxxxxxxxxxxxx<br>xxxxxxxxxxxxxxxxxxxx</p>
</section>

<section class="card card--kelpora">
  <svg class="card__band" viewBox="0 0 510 290" aria-hidden="true">
    <defs>
      <linearGradient id="kelpora-band" x1="0" y1="0" x2="1" y2="0">
        <stop offset="0" stop-color="var(--blue-light)"/>
        <stop offset="1" stop-color="var(--blue-deep)"/>
      </linearGradient>
    </defs>
    <path d="M0 0H510V140C420 92 270 40 0 34Z" fill="url(#kelpora-band)"/>
    <path d="M0 40C120 26 250 32 390 70C250 40 120 38 0 54Z" fill="var(--green)"/>
  </svg>
  <p class="card__holder">Your Name <span>/ Title</span></p>
  <div class="brand"><span class="brand__mark"></span><span class="brand__name">Kelpora</span></div>
  <p class="brand__tagline">Professional SEO Services</p>
  <ul class="contact">
    <li><svg viewBox="0 0 10 10"><path d="M2 0l2 2-1 1.5c.6 1.3 1.6 2.3 2.9 2.9L7 5l2 2-1.4 1.8C4 8.6 1.3 6 1 2.3Z"/></svg>123-456-7890</li>
    <li><svg viewBox="0 0 10 10"><rect x="2.5" y="0" width="5" height="10" rx="1"/></svg>123-456-7890</li>
    <li><svg viewBox="0 0 10 10"><path d="M0 4h10v2H7V5H3v1H0Z"/><rect x="2" y="6" width="6" height="4" rx="1"/></svg>123-456-7890</li>
    <li><svg viewBox="0 0 10 10"><path d="M0 2h10v6H0Z"/></svg>name@website.com</li>
    <li><svg viewBox="0 0 10 10"><circle cx="5" cy="5" r="5"/></svg>www.website.com</li>
  </ul>
  <p class="address">Complex name, Street<br>City, State, zip code</p>
  <p class="extra">xxxxxxxxxxxxxxxxxxxx<br>xxxxxxxxxxxxxxxxxxxx</p>
</section>

</body>
</html>
```